Graphic Design for Flavoured Drink product

I need a packaging design for flavoured drinks product.
The product is a mix of Sparkling Natural Mineral Water (from France) with other flavouring.

There will be various flavours i.e. apple, orange, strawberry, etc.
However, you may design the product using one sample flavour first, as the designs of other flavours could be adjusted afterwards.

The temporary product name is: QUIVLO

I want the product design to be something 'fun' and 'colourful'.
The design concept could be anything depends on your imagination.
Basically, I want you to be creative in designing the logo and the overall graphic design for the label.

- Create something different. Something extraordinary -

Thank you and Good Luck!

Additional:

The measurement is 20cm (Length) x 10cm (Height).

The target customers are young audiences (10 years - 35 years old).

I am hoping to have a product design that can stand out in the supermarket shelf.
It must be eye catchy and attractive.

Thank you,
Marcus

-PLEASE REFER TO DESIGN SAMPLE ATTACHED TO HAVE A BETTER UNDERSTANDING FOR THE PRODUCT CONCEPT-

Reason: I havent found any satisfactory designs so far. Please submit much better quality designs. Thank you, Marcus

```html
<!DOCTYPE html>
<html lang="en">
<head>
<meta charset="utf-8">
<title>QUIVLO – Flavoured Sparkling Natural Mineral Water labels</title>
<link rel="stylesheet" href="https://fonts.googleapis.com/css2?family=Josefin+Sans:wght@100;300&family=Raleway:wght@400&display=swap">
<style>
  :root {
    --ink: #1b1b1b;
    --tagline: #5a5a5a;
    --glow: #ffffff;
    --strawberry: #f2434f;
    --strawberry-text: #e8364a;
    --apple: #86e21a;
    --apple-text: #7fd321;
    --orange: #f88d26;
    --orange-text: #f7962e;
  }
  * { margin: 0; padding: 0; box-sizing: border-box; }
  html, body {
    width: 801px;
    height: 1200px;
    overflow: hidden;
    background: #ffffff;
  }
  .label-set {
    width: 801px;
    height: 1200px;
    display: flex;
    flex-direction: column;
  }
  .label {
    position: relative;
    width: 801px;
    height: 400px;
    overflow: hidden;
  }
  .label__backdrop {
    position: absolute;
    inset: 0;
  }
  .label--strawberry .label__backdrop {
    background: radial-gradient(ellipse 62% 70% at 56% 34%, var(--glow) 0%, #fbd3d6 28%, #f78a92 62%, var(--strawberry) 100%);
  }
  .label--apple .label__backdrop {
    background: radial-gradient(ellipse 62% 70% at 56% 36%, var(--glow) 0%, #e3f8c8 28%, #b6ef6a 62%, var(--apple) 100%);
  }
  .label--orange .label__backdrop {
    background: radial-gradient(ellipse 62% 70% at 56% 36%, var(--glow) 0%, #fde2c4 28%, #fbb26a 62%, var(--orange) 100%);
  }
  .brand-block {
    position: absolute;
    left: 198px;
    top: 146px;
    width: 404px;
    display: flex;
    flex-direction: column;
  }
  .brand-name {
    font-family: "Josefin Sans", sans-serif;
    font-weight: 100;
    font-size: 90px;
    line-height: 72px;
    height: 72px;
    letter-spacing: 9px;
    color: var(--ink);
    white-space: nowrap;
    text-align: center;
  }
  .tagline {
    margin-top: 12px;
    font-family: "Raleway", sans-serif;
    font-weight: 400;
    font-size: 16.5px;
    line-height: 20px;
    color: var(--tagline);
    white-space: nowrap;
    text-align: center;
  }
  .flavour {
    margin-top: 13px;
    align-self: flex-end;
    display: flex;
    align-items: center;
    gap: 6px;
    font-family: "Raleway", sans-serif;
    font-weight: 400;
    font-size: 25px;
    line-height: 28px;
    letter-spacing: 0.5px;
  }
  .flavour__dot {
    width: 21px;
    height: 21px;
    border-radius: 50%;
    flex: none;
  }
  .label--strawberry .flavour { color: var(--strawberry-text); }
  .label--strawberry .flavour__dot { background: var(--strawberry-text); }
  .label--apple .flavour { color: var(--apple-text); }
  .label--apple .flavour__dot { background: var(--apple-text); }
  .label--orange .flavour { color: var(--orange-text); }
  .label--orange .flavour__dot { background: var(--orange-text); }
</style>
</head>
<body>
<main class="label-set">
  <section class="label label--strawberry">
    <div class="label__backdrop" role="img" aria-label="Soft red backdrop with glowing bokeh bubbles"></div>
    <div class="brand-block">
      <h1 class="brand-name">QUIVLO</h1>
      <p class="tagline">Flavoured Sparkling Natural Mineral Water</p>
      <p class="flavour"><span class="flavour__dot"></span>STRAWBERRY</p>
    </div>
  </section>
  <section class="label label--apple">
    <div class="label__backdrop" role="img" aria-label="Soft green backdrop with glowing bokeh bubbles"></div>
    <div class="brand-block">
      <h2 class="brand-name">QUIVLO</h2>
      <p class="tagline">Flavoured Sparkling Natural Mineral Water</p>
      <p class="flavour"><span class="flavour__dot"></span>APPLE</p>
    </div>
  </section>
  <section class="label label--orange">
    <div class="label__backdrop" role="img" aria-label="Soft orange backdrop with glowing bokeh bubbles"></div>
    <div class="brand-block">
      <h2 class="brand-name">QUIVLO</h2>
      <p class="tagline">Flavoured Sparkling Natural Mineral Water</p>
      <p class="flavour"><span class="flavour__dot"></span>ORANGE</p>
    </div>
  </section>
</main>
</body>
</html>
```